Brivora Collective Business Card Design

We need a business card design for Brivora Collective. We are a healthcare recruiting, wellness and education company. We partner with medical facilities to find quality candidates. We also offer free wellness courses.
The final design should communicate an emphasis on recruiting and wellness
The main purpose of the business card is to utilized it for networking events, give to hospitals, executives, VCs surgery centers and clinics. I want it to be sleek, clean, use of our brand colors and professional.

```html
<!DOCTYPE html>
<html lang="en">
<head>
<meta charset="utf-8">
<title>Brivora Collective Business Card</title>
<link rel="stylesheet" href="https://fonts.googleapis.com/css2?family=Arimo:wght@400&family=Montserrat:wght@700&display=swap">
<style>
  :root {
    --page-bg: #1d1d1d;
    --card-bg: #111111;
    --teal: #00b3a7;
    --white: #f4f4f4;
    --rule: #3a3a3a;
    --pattern-dark: #151515;
    --pattern-light: #3c3c3c;
  }
  * { box-sizing: border-box; margin: 0; padding: 0; }
  html, body { width: 1200px; height: 1108px; overflow: hidden; }
  body {
    background: var(--page-bg);
    display: flex;
    align-items: center;
    justify-content: center;
    gap: 70px;
    font-family: "Arimo", Arial, sans-serif;
  }
  .card {
    width: 470px;
    height: 740px;
    border-radius: 26px;
    background: var(--card-bg);
    box-shadow: 0 20px 40px rgba(0,0,0,0.45);
    overflow: hidden;
    position: relative;
  }
  .card-front {
    display: flex;
    flex-direction: column;
    align-items: center;
    padding-top: 150px;
    color: var(--white);
    text-align: center;
  }
  .brand {
    display: flex;
    align-items: center;
    gap: 14px;
    color: var(--teal);
    font-size: 40px;
    font-weight: 400;
    line-height: 1.1;
  }
  .brand-square {
    width: 26px;
    height: 26px;
    background: var(--teal);
    border-radius: 5px;
    flex: none;
  }
  .person { margin-top: 100px; }
  .person-name {
    font-family: "Montserrat", Arial, sans-serif;
    font-weight: 700;
    color: var(--teal);
    font-size: 32px;
    letter-spacing: 0.5px;
  }
  .person-title { font-size: 22px; margin-top: 4px; }
  .contact-divider {
    width: 300px;
    margin-top: 26px;
    display: flex;
    align-items: center;
    gap: 12px;
  }
  .contact-divider::before,
  .contact-divider::after {
    content: "";
    flex: 1;
    height: 1px;
    background: var(--rule);
  }
  .contact-icons { display: flex; gap: 10px; }
  .contact-icon { width: 26px; height: 26px; }
  .contact-list {
    list-style: none;
    margin-top: 18px;
    font-size: 21px;
    line-height: 1.35;
  }
  .address-rule {
    width: 300px;
    height: 1px;
    background: var(--rule);
    margin-top: 22px;
  }
  .address {
    font-style: normal;
    font-size: 21px;
    line-height: 1.35;
    margin-top: 22px;
  }
  .card-back .pattern-fill {
    position: absolute;
    inset: 0;
    background: linear-gradient(135deg, var(--pattern-dark) 0%, #222 50%, var(--pattern-light) 100%);
  }
</style>
</head>
<body>
  <section class="card card-front" aria-label="Card front">
    <div class="brand">
      <span class="brand-square" aria-hidden="true"></span>
      <span class="brand-name">Brivora Collective</span>
    </div>

    <div class="person">
      <h1 class="person-name">Daniel Hart</h1>
      <p class="person-title">President</p>
    </div>

    <div class="contact-divider">
      <div class="contact-icons">
        <svg class="contact-icon" viewBox="0 0 26 26" aria-label="Phone">
          <rect width="26" height="26" rx="6" fill="var(--teal)"/>
          <path d="M9 7c1 0 1.5 2.5 1.5 3s-1 1-1 1.5c.5 1.8 2.2 3.5 4 4 .5 0 1-1 1.5-1s3 .5 3 1.5-1 2-2 2C11 18 8 15 8 9c0-1 0-2 1-2z" fill="#fff"/>
        </svg>
        <svg class="contact-icon" viewBox="0 0 26 26" aria-label="Email">
          <rect width="26" height="26" rx="6" fill="var(--teal)"/>
          <rect x="6" y="8.5" width="14" height="9.5" rx="1" fill="#fff"/>
          <path d="M6.5 9l6.5 5 6.5-5" fill="none" stroke="var(--teal)" stroke-width="1.3"/>
        </svg>
        <svg class="contact-icon" viewBox="0 0 26 26" aria-label="Website">
          <rect width="26" height="26" rx="6" fill="var(--teal)"/>
          <circle cx="13" cy="13" r="6.5" fill="none" stroke="#fff" stroke-width="1.5"/>
          <ellipse cx="13" cy="13" rx="2.8" ry="6.5" fill="none" stroke="#fff" stroke-width="1.2"/>
          <line x1="6.5" y1="13" x2="19.5" y2="13" stroke="#fff" stroke-width="1.2"/>
        </svg>
      </div>
    </div>

    <ul class="contact-list">
      <li>(555) 0142-7781</li>
      <li>name@brivoracollective.com</li>
      <li>www.brivoracollective.com</li>
    </ul>

    <div class="address-rule" aria-hidden="true"></div>

    <address class="address">
      4127 Alder Crest Lane<br>
      Lakeview, NY 11590
    </address>
  </section>

  <section class="card card-back" aria-label="Card back">
    <div class="pattern-fill" role="img" aria-label="Glossy tonal repeat pattern of the brand symbol across the black card back"></div>
  </section>
</body>
</html>
```